Lanterne architecture business cards

We are a new company based in New Zealand. We Specialize in High end Luxury Residential Architecture.

Every home is bespoke and is designed to each clients individual requirements and needs.

I like to design buildings that inspire people through light and form while offering a high level of comfort and usability.

Lines of sight, proportion and balance are fundamental to the spaces I create.
Updates

August 5th is current deadline - Today's date is the 13th of August.

Target Market(s)

New Zealanders who want a custom individual home design, typically 30-65 year old males and females

Industry/Entity Type

Architecture

Contact Information for Business Card

Director - Derek Tolson
Contact Number - 0279164073
Email - info@lanternearchitecture-example.co.nz
Webstie - www.lanternearchitecture-example.co.nz
Social Media - @lanternearchitecture

Font styles to use
Sans Serif

Requirements
Must have
• Logo (Both Sides)
Website
Email
Contact Number
Social Media

Nice to have
• Texture
Should not have
• More than 3 colours - typically I would've thought 2 would be good to match the logo.

```html
<!DOCTYPE html>
<html lang="en">
<head>
<meta charset="utf-8">
<title>Lanterne architecture – business cards</title>
<link rel="stylesheet" href="https://fonts.googleapis.com/css2?family=Montserrat:wght@400;500;700&display=swap">
<style>
  :root {
    --backdrop: #d6d6d6;
    --card: #ffffff;
    --ink: #111111;
    --silver: #a6a6a6;
    --shadow: rgba(0, 0, 0, 0.18);
  }
  * { box-sizing: border-box; margin: 0; padding: 0; }
  html, body {
    width: 1200px;
    height: 900px;
    overflow: hidden;
    background: var(--backdrop);
    font-family: "Montserrat", Arial, sans-serif;
    color: var(--ink);
  }
  .canvas {
    width: 1200px;
    height: 900px;
    display: flex;
    flex-direction: column;
    align-items: center;
    justify-content: center;
    gap: 40px;
  }
  .card {
    position: relative;
    width: 700px;
    height: 400px;
    background: var(--card);
    box-shadow: 0 10px 28px var(--shadow);
  }

  /* Front */
  .card--front {
    display: flex;
    align-items: center;
    justify-content: center;
  }
  .wordmark {
    font-weight: 400;
    font-size: 30px;
    letter-spacing: 0.32em;
    text-transform: uppercase;
    color: var(--silver);
  }

  /* Back */
  .brand-block {
    position: absolute;
    left: 60px;
    top: 92px;
    width: 220px;
    display: flex;
    flex-direction: column;
    align-items: center;
    gap: 18px;
  }
  .brand-dot {
    width: 120px;
    height: 120px;
    border-radius: 50%;
    background: var(--silver);
  }
  .brand-name {
    font-weight: 400;
    font-size: 15px;
    letter-spacing: 0.18em;
    text-transform: uppercase;
    text-align: center;
    color: var(--silver);
  }
  .contact {
    position: absolute;
    left: 320px;
    top: 120px;
  }
  .contact__name {
    font-weight: 700;
    font-size: 26px;
    letter-spacing: 0.02em;
    text-transform: uppercase;
    line-height: 1;
  }
  .contact__role {
    font-weight: 500;
    font-size: 16px;
    margin-top: 4px;
  }
  .contact__list {
    list-style: none;
    margin-top: 22px;
  }
  .contact__item {
    display: flex;
    align-items: center;
    gap: 10px;
    font-weight: 500;
    font-size: 15px;
    line-height: 26px;
  }
  .contact__icon {
    width: 16px;
    height: 16px;
    flex: none;
  }
  .social {
    position: absolute;
    left: 170px;
    bottom: 44px;
    display: flex;
    align-items: center;
    gap: 10px;
    font-weight: 500;
    font-size: 17px;
  }
  .social__dot {
    width: 12px;
    height: 12px;
    border-radius: 50%;
    background: var(--ink);
  }
</style>
</head>
<body>
  <main class="canvas">
    <section class="card card--front" aria-label="Card front">
      <p class="wordmark">Lanterne architecture</p>
    </section>

    <section class="card card--back" aria-label="Card back">
      <div class="brand-block">
        <span class="brand-dot" aria-hidden="true"></span>
        <p class="brand-name">Lanterne architecture</p>
      </div>

      <div class="contact">
        <h1 class="contact__name">Derek Tolson</h1>
        <p class="contact__role">Director</p>
        <ul class="contact__list">
          <li class="contact__item">
            <svg class="contact__icon" viewBox="0 0 24 24" aria-hidden="true">
              <path fill="#111" d="M6.6 10.8a15.1 15.1 0 0 0 6.6 6.6l2.2-2.2a1 1 0 0 1 1-.25 11.4 11.4 0 0 0 3.6.57 1 1 0 0 1 1 1V20a1 1 0 0 1-1 1A17 17 0 0 1 3 4a1 1 0 0 1 1-1h3.5a1 1 0 0 1 1 1c0 1.25.2 2.45.57 3.57a1 1 0 0 1-.25 1z"/>
            </svg>
            <span>0279164073</span>
          </li>
          <li class="contact__item">
            <svg class="contact__icon" viewBox="0 0 24 24" aria-hidden="true">
              <rect x="2.5" y="5" width="19" height="14" fill="none" stroke="#111" stroke-width="2"/>
              <path d="M3 6l9 7 9-7" fill="none" stroke="#111" stroke-width="2"/>
            </svg>
            <span>info@lanternearchitecture-example.co.nz</span>
          </li>
          <li class="contact__item">
            <svg class="contact__icon" viewBox="0 0 24 24" aria-hidden="true">
              <g fill="none" stroke="#111" stroke-width="1.8">
                <circle cx="12" cy="12" r="9"/>
                <ellipse cx="12" cy="12" rx="4" ry="9"/>
                <path d="M3 12h18M5 7h14M5 17h14"/>
              </g>
            </svg>
            <span>www.lanternearchitecture-example.co.nz</span>
          </li>
        </ul>
      </div>

      <p class="social">
        <span class="social__dot" aria-hidden="true"></span>
        <span>@lanternearchitecture</span>
      </p>
    </section>
  </main>
</body>
</html>
```